Business Card Design for Cloud Frames

Hi we need a business card designed for a new aerial photography business we have started, we use UAV Drones to take photos for corporate, events, real estate, local government etc , the business name is Cloud Frames Australia, we have a facebook page that might help you come up with some designs - https://www.facebook.com/cloudframesaustralia

We need to have and editable AI file so that we can use different names and contact details. details for one of the cards as follow:

Dave Marsh
phone: 03 5512 4837
Mobile: 0439 175 286
email: dave@cloudframes.example.com.au
web: www.cloudframes.example.com.au

have now changed: Designer Payment:Committed

Target Market(s)

We are a Aerial Photography business using Drones and UAV

Industry/Entity Type

Business

Logo Text

Cloud Frames Australia

Requirements
Must have
• Colors to match logo and be part of Cloud Frames Brand

```html
<!DOCTYPE html>
<html lang="en">
<head>
<meta charset="utf-8">
<title>Cloud Frames Australia – Business Card</title>
<link rel="stylesheet" href="https://fonts.googleapis.com/css2?family=Orbitron:wght@500;700&display=swap">
<style>
  :root {
    --page: #ffffff;
    --card-top: #46505d;
    --card-bottom: #2a3038;
    --slot: #1c1f24;
    --slot-edge: #5a6370;
    --silver: #c3c7cc;
    --accent: #29b2e6;
    --beam: #4aa6e0;
  }
  * { margin: 0; padding: 0; box-sizing: border-box; }
  html, body {
    width: 857px; height: 1200px; overflow: hidden;
    background: var(--page);
  }
  .sheet { position: relative; width: 857px; height: 1200px; }
  .card {
    position: absolute; left: 29px; width: 799px; height: 556px;
    border-radius: 22px; overflow: hidden;
    background: radial-gradient(ellipse at 55% 20%, var(--card-top) 0%, var(--card-bottom) 85%);
    font-family: "Orbitron", sans-serif;
  }
  .card--front { top: 22px; }
  .card--back { top: 622px; }
  .card__deco { position: absolute; inset: 0; }
  .wordmark {
    position: absolute; color: var(--silver);
    font-weight: 700; font-size: 34px; line-height: 1.12;
    letter-spacing: 2px; text-transform: uppercase;
  }
  .card--front .wordmark { left: 34px; top: 36px; }
  .card--back .wordmark { left: 0; right: 0; top: 188px; text-align: center; }
  .holder {
    position: absolute; left: 259px; top: 262px;
    color: var(--accent); font-weight: 700; font-size: 31px;
    letter-spacing: 1px; word-spacing: 10px; text-transform: uppercase;
  }
  .contact {
    position: absolute; left: 273px; top: 342px;
    list-style: none; color: var(--silver);
    font-weight: 700; font-size: 17px; line-height: 36px;
    letter-spacing: 1px; text-transform: uppercase;
  }
  .contact__label { margin-right: 10px; }
</style>
</head>
<body>
<main class="sheet">
  <section class="card card--front" aria-label="Card front">
    <svg class="card__deco" width="799" height="556" viewBox="0 0 799 556" aria-hidden="true">
      <defs>
        <linearGradient id="beamFade" x1="0" y1="0" x2="1" y2="0">
          <stop offset="0" stop-color="var(--beam)" stop-opacity="0.55"/>
          <stop offset="0.6" stop-color="var(--beam)" stop-opacity="0.25"/>
          <stop offset="1" stop-color="var(--beam)" stop-opacity="0.05"/>
        </linearGradient>
      </defs>
      <polygon points="0,0 799,0 799,40 0,120" fill="url(#beamFade)" opacity="0.7"/>
      <polygon points="0,60 799,110 799,160 0,95" fill="url(#beamFade)" opacity="0.35"/>
      <line x1="0" y1="110" x2="799" y2="155" stroke="var(--beam)" stroke-opacity="0.6" stroke-width="1.5"/>
      <line x1="0" y1="72" x2="799" y2="25" stroke="var(--beam)" stroke-opacity="0.4" stroke-width="1"/>
      <rect x="734" y="0" width="40" height="261" fill="var(--slot)" stroke="var(--slot-edge)" stroke-opacity="0.5"/>
      <rect x="0" y="448" width="261" height="38" fill="var(--slot)"/>
      <line x1="0" y1="486" x2="261" y2="486" stroke="var(--slot-edge)"/>
      <line x1="261" y1="448" x2="799" y2="448" stroke="var(--slot)" stroke-width="2"/>
      <line x1="261" y1="450" x2="799" y2="450" stroke="var(--slot-edge)" stroke-opacity="0.6"/>
      <line x1="261" y1="448" x2="261" y2="486" stroke="var(--slot-edge)" stroke-opacity="0.6"/>
    </svg>
    <div class="wordmark">Cloud<br>Frames<br>Australia</div>
    <h1 class="holder">Dave Marsh</h1>
    <ul class="contact">
      <li><span class="contact__label">Phone:</span>03 5512 4837</li>
      <li><span class="contact__label">Mobile:</span>0439 175 286</li>
      <li><span class="contact__label">Email:</span>dave@cloudframes.example.com.au</li>
      <li><span class="contact__label">Web:</span>www.cloudframes.example.com.au</li>
    </ul>
  </section>

  <section class="card card--back" aria-label="Card back">
    <svg class="card__deco" width="799" height="556" viewBox="0 0 799 556" aria-hidden="true">
      <rect x="48" y="0" width="40" height="271" fill="var(--slot)" stroke="var(--slot-edge)" stroke-opacity="0.5"/>
      <line x1="0" y1="436" x2="799" y2="436" stroke="var(--slot)" stroke-width="2"/>
      <line x1="0" y1="438" x2="799" y2="438" stroke="var(--slot-edge)" stroke-opacity="0.6"/>
      <rect x="563" y="438" width="236" height="34" fill="var(--slot)"/>
      <line x1="563" y1="472" x2="799" y2="472" stroke="var(--slot-edge)"/>
    </svg>
    <div class="wordmark">Cloud<br>Frames<br>Australia</div>
  </section>
</main>
</body>
</html>
```